K7Q480 brochure

We want a new brochure for our rebranding of our sports health and wellness centre. We are based in Townsville in North Queensland. We provide chiropractic, physiotherapy, massage, nutrition and yoga services. We would like to see designs and content that portray our unique one stop destination for many allied health services and our one on one functional rehab approach customised to each individual. We would like to keep colours that compliment our logo colours. The design should be professional and one that could be handed out to Medical Doctors, other referring healthcare professionals and prospective sports and active lifestyle patients. The brochure should also note that we also accept/treat Jobshield, RSB, Vitafund KPS, and Accident and Injury referrals
Updates

Please check out our website for more information on who we are and what we do. I will upload our new logo in a few moments. Cheers! Www.peakvitaro.com.au

Reason: We understand creating a quality brochure takes time and we wanted to give the creatives more time to create. With the extended deadline we are now guaranteeing the payment.

Target Market(s)

Referring Medical Doctors and other health professionals
Athletes and Active lifestyle patients
Wellness patients

Industry/Entity Type

Healthcare

Requirements
Nice to have
• Brochure can be single double sided, or bi-fold of approx. size of 210mm x 99mm
Should not have
• Brochure should not focus on or place emphasis on one particular service that we offer rather focus on the services provided as a whole.

```html
<!DOCTYPE html>
<html lang="en">
<head>
<meta charset="utf-8">
<title>K7Q480 – Brochure Services Spread</title>
<link href="https://fonts.googleapis.com/css2?family=Didact+Gothic&family=Questrial&display=swap" rel="stylesheet">
<style>
  :root {
    --grass-light: #7fc24a;
    --grass-mid: #4f9a2a;
    --grass-dark: #2f6e17;
    --text: #ffffff;
    --shadow: rgba(20, 50, 10, 0.9);
    --rule: rgba(255, 255, 255, 0.55);
  }
  html, body {
    margin: 0;
    padding: 0;
    overflow: hidden;
  }
  body {
    width: 1200px;
    height: 566px;
  }
  .brochure-spread {
    position: relative;
    width: 1200px;
    height: 566px;
    overflow: hidden;
    font-family: "Didact Gothic", "Questrial", sans-serif;
    color: var(--text);
  }
  .lawn-backdrop {
    position: absolute;
    inset: 0;
    background:
      radial-gradient(ellipse at 70% 10%, rgba(180, 230, 120, 0.5), transparent 55%),
      radial-gradient(ellipse at 20% 90%, rgba(30, 80, 15, 0.5), transparent 60%),
      linear-gradient(170deg, var(--grass-light) 0%, var(--grass-mid) 50%, var(--grass-dark) 100%);
  }
  .service {
    position: absolute;
    width: 530px;
  }
  .service-photo {
    position: absolute;
    left: 0;
    top: 0;
    width: 110px;
    height: 110px;
    border-radius: 9px;
    box-shadow: 0 1px 4px rgba(0, 0, 0, 0.35);
  }
  .service-body {
    position: absolute;
    left: 129px;
    top: -2px;
    width: 395px;
  }
  .service-title {
    margin: 0 0 15px;
    font-family: "Questrial", sans-serif;
    font-weight: 400;
    font-size: 15px;
    line-height: 18px;
    letter-spacing: 0.2px;
    text-shadow: 0.4px 0 0 var(--text), 1px 1px 2px var(--shadow);
  }
  .service-text {
    margin: 0;
    font-size: 16.2px;
    line-height: 16.4px;
    letter-spacing: 0.45px;
    text-shadow: 1px 1px 2px var(--shadow), 0 0 3px var(--shadow);
  }
  .col-left { left: 46px; }
  .col-right { left: 645px; }
  .row-1 { top: 46px; }
  .row-2 { top: 199px; }
  .row-3 { top: 352px; }

  .photo-chiro { background: linear-gradient(135deg, #e7b99a, #b9775a); }
  .photo-fruit { background: linear-gradient(135deg, #d9412b, #f2b632 55%, #5c8c2c); }
  .photo-exercise { background: linear-gradient(135deg, #f4f1ee, #c9a58c); }
  .photo-massage { background: linear-gradient(135deg, #e9c9a9, #9a6a4c); }
  .photo-yoga { background: linear-gradient(180deg, #4f8fd6 0%, #8ec0ee 55%, #5c9a32 75%, #3e7a22 100%); }
  .photo-posture { background: linear-gradient(135deg, #b07a5c, #5e3a28); }

  .referral-strip {
    position: absolute;
    left: 46px;
    right: 46px;
    top: 518px;
    padding-top: 9px;
    border-top: 1px solid var(--rule);
    display: flex;
    justify-content: space-between;
    font-size: 13.5px;
    letter-spacing: 0.3px;
    text-shadow: 1px 1px 2px var(--shadow), 0 0 3px var(--shadow);
  }
  .referral-strip strong {
    font-family: "Questrial", sans-serif;
    font-weight: 400;
    text-shadow: 0.4px 0 0 var(--text), 1px 1px 2px var(--shadow);
  }
</style>
</head>
<body>
<main class="brochure-spread">
  <div class="lawn-backdrop" role="img" aria-label="Close-up photograph of fresh green lawn grass"></div>

  <section class="service col-left row-1">
    <div class="service-photo photo-chiro" role="img" aria-label="Photo of hands performing a chiropractic adjustment on a shoulder"></div>
    <div class="service-body">
      <h2 class="service-title">Chiropractic Care</h2>
      <p class="service-text">We provide advanced spinal correction and chiropractic adjustments utilizing "state of the art" chiropractic techniques. Never in the history of chiropractic care have chiropractors been able to provide the level of help and expertise that is available today.</p>
    </div>
  </section>

  <section class="service col-left row-2">
    <div class="service-photo photo-exercise" role="img" aria-label="Photo of a woman lifting a dumbbell"></div>
    <div class="service-body">
      <h2 class="service-title">Corrective Exercises</h2>
      <p class="service-text">At K7Q480, we teach our patients how to perform special "blueprint" exercises which can help strengthen and correct the irregularities in their body which may be causing pain.</p>
    </div>
  </section>

  <section class="service col-left row-3">
    <div class="service-photo photo-yoga" role="img" aria-label="Photo of a woman in a yoga warrior pose on grass under blue sky"></div>
    <div class="service-body">
      <h2 class="service-title">Lifestyle Advice and In house Yoga</h2>
      <p class="service-text">Many of our patients come to see our chiropractor to address a specific pain symptom such as back pain, neck pain or headaches. While our chiropractor will address each patient's specific condition with chiropractic care, we often find it helpful to "coach" our patients towards achieving a healthier lifestyle.</p>
    </div>
  </section>

  <section class="service col-right row-1">
    <div class="service-photo photo-fruit" role="img" aria-label="Photo of fresh vegetables: capsicums, tomatoes and greens"></div>
    <div class="service-body">
      <h2 class="service-title">Nutritional Counselling</h2>
      <p class="service-text">What does nutrition have to do with chiropractic care? The goal of chiropractic care is to help patients achieve total health and balance with their body, and as part of that goal we provide specific recommendations on nutritional supplements and healthy food choices.</p>
    </div>
  </section>

  <section class="service col-right row-2">
    <div class="service-photo photo-massage" role="img" aria-label="Photo of a woman receiving a back massage"></div>
    <div class="service-body">
      <h2 class="service-title">Massage Therapy</h2>
      <p class="service-text">Massage therapy does more than make you feel good, it can actually help your body achieve balance and health. Massage therapy offers a natural treatment approach which actually relieves musculoskeletal pain for many patients.</p>
    </div>
  </section>

  <section class="service col-right row-3">
    <div class="service-photo photo-posture" role="img" aria-label="Photo of a man's bare back and shoulders, hands behind head"></div>
    <div class="service-body">
      <h2 class="service-title">Spinal &amp; Postural Screenings</h2>
      <p class="service-text">There is a saying that an ounce of prevention is worth a pound of cure. Your spinal health is no exception. Posture and spinal screenings by a trained and experienced chiropractor such as Dr. Lena Marsh can help reveal important health information, unlocking the door to improved health and well-being.</p>
    </div>
  </section>

  <footer class="referral-strip">
    <span><strong>One stop:</strong> Chiropractic · Physiotherapy · Massage · Nutrition · Yoga</span>
    <span><strong>We accept</strong> Jobshield, RSB, Vitafund KPS and Accident &amp; Injury referrals</span>
  </footer>
</main>
</body>
</html>
```